T6 Construction Site Sign

I would like to get a sign designed which would be installed at a construction sign. I would like to incorporate my current logo, font and colors in the sign. The sign would be 30" x 60" (vertical). Would like to keep it clean and simple yet eye catching and sparks interest. I have attached my branding colors. I would like the background to be the branded blue with white text.

```html
<!DOCTYPE html>
<html lang="en">
<head>
<meta charset="utf-8">
<title>T6 Contracting &amp; Development Ltd. – Site Sign</title>
<link href="https://fonts.googleapis.com/css2?family=Poppins:wght@300;500&display=swap" rel="stylesheet">
<style>
  :root {
    --brand-blue: #2f5b94;
    --brand-orange: #eaa541;
    --sign-white: #ffffff;
    --page-bg: #eceef1;
    --photo-sky: #c9b6d6;
    --photo-house: #5d6f8f;
  }
  * { box-sizing: border-box; margin: 0; padding: 0; }
  html, body {
    width: 1159px;
    height: 1200px;
    overflow: hidden;
    background: var(--page-bg);
    font-family: "Poppins", sans-serif;
  }
  .sign {
    position: absolute;
    left: 279px;
    top: 0;
    width: 600px;
    height: 1200px;
    background: var(--sign-white);
    overflow: hidden;
  }
  .sign-shapes {
    position: absolute;
    inset: 0;
  }
  .brand {
    position: absolute;
    left: 34px;
    top: 132px;
    display: flex;
    align-items: center;
    gap: 14px;
    color: var(--brand-blue);
  }
  .brand-square {
    flex: none;
    width: 16px;
    height: 16px;
    background: var(--brand-blue);
  }
  .brand-name {
    font-weight: 300;
    font-size: 30px;
    line-height: 1.15;
    letter-spacing: 0.5px;
  }
  .services {
    position: absolute;
    left: 58px;
    top: 668px;
    list-style: none;
    color: var(--sign-white);
    font-weight: 500;
    font-size: 23px;
  }
  .services li {
    display: flex;
    align-items: center;
    gap: 16px;
    height: 58px;
  }
  .services svg { flex: none; }
  .contact {
    position: absolute;
    left: 58px;
    top: 1040px;
    color: var(--brand-blue);
  }
  .contact-line {
    display: flex;
    align-items: center;
    gap: 12px;
    font-weight: 500;
    line-height: 1;
  }
  .contact-phone { font-size: 50px; margin-bottom: 22px; letter-spacing: 1px; }
  .contact-web { font-size: 44px; }
</style>
</head>
<body>
  <div class="sign">
    <svg class="sign-shapes" width="600" height="1200" viewBox="0 0 600 1200">
      <defs>
        <linearGradient id="photo-tone" x1="0" y1="0" x2="0" y2="1">
          <stop offset="0" stop-color="var(--photo-sky)"/>
          <stop offset="0.55" stop-color="var(--photo-house)"/>
          <stop offset="1" stop-color="#8a8f9c"/>
        </linearGradient>
      </defs>
      <polygon class="corner-accent" points="410,0 600,0 600,175" fill="var(--brand-orange)"/>
      <g class="project-photos" role="img" aria-label="Photo collage of a newly built two-storey house with garage at dusk" fill="url(#photo-tone)">
        <rect x="30" y="290" width="150" height="142"/>
        <rect x="190" y="258" width="160" height="164"/>
        <rect x="360" y="232" width="180" height="148"/>
        <rect x="30" y="442" width="150" height="150"/>
        <polygon points="190,432 352,566 190,580"/>
        <polygon points="362,392 540,380 364,584"/>
      </g>
      <polygon class="side-accent" points="540,420 425,555 545,652" fill="var(--brand-orange)"/>
      <polygon class="service-band" points="0,612 380,588 600,800 600,1000 0,1020" fill="var(--brand-blue)"/>
    </svg>

    <div class="brand">
      <span class="brand-square" aria-hidden="true"></span>
      <span class="brand-name">T6 Contracting &amp;<br>Development Ltd.</span>
    </div>

    <ul class="services">
      <li><svg width="18" height="18" viewBox="0 0 18 18"><polygon points="18,0 18,18 0,18" fill="#fff"/></svg>Custom Homes</li>
      <li><svg width="18" height="18" viewBox="0 0 18 18"><polygon points="18,0 18,18 0,18" fill="#fff"/></svg>Commercial/Retail</li>
      <li><svg width="18" height="18" viewBox="0 0 18 18"><polygon points="18,0 18,18 0,18" fill="#fff"/></svg>Land Development Consulting</li>
      <li><svg width="18" height="18" viewBox="0 0 18 18"><polygon points="18,0 18,18 0,18" fill="#fff"/></svg>Construction Project Management</li>
    </ul>

    <div class="contact">
      <div class="contact-line contact-phone">
        <svg width="26" height="26" viewBox="0 0 24 24" aria-hidden="true"><path d="M6.6 10.8a15.1 15.1 0 0 0 6.6 6.6l2.2-2.2a1 1 0 0 1 1-.25 11.4 11.4 0 0 0 3.6.57 1 1 0 0 1 1 1V20a1 1 0 0 1-1 1A17 17 0 0 1 3 4a1 1 0 0 1 1-1h3.5a1 1 0 0 1 1 1c0 1.25.2 2.45.57 3.57a1 1 0 0 1-.25 1z" fill="var(--brand-orange)"/></svg>
        1 604-555-0182
      </div>
      <div class="contact-line contact-web">
        <svg width="26" height="26" viewBox="0 0 24 24" aria-hidden="true"><circle cx="12" cy="12" r="10" fill="none" stroke="var(--brand-orange)" stroke-width="2"/><path d="M2 12h20M12 2c3 3 3 17 0 20M12 2c-3 3-3 17 0 20" fill="none" stroke="var(--brand-orange)" stroke-width="2"/></svg>
        T6contracting.com
      </div>
    </div>
  </div>
</body>
</html>
```